Exhibition Stand Design for innovative Social Business

We are an innovative social business empowering people to value nature through ZUN, a complementary digital currency. We have attached the TEK_ZUN branding document, and are needing a design for our exhibition stand (https://fairbuildlab.com/produit/stand-parapluie-classic-pvc-3x4c/. The attached doc mocks up a stand on page 32, though we would like some messaging included, in line with our website www.tekzun.ch. You will see there how the branding concept has been implemented with the TEK:GROW, SHARE, THRIVE wording, as well as Everyone wins. Our green colours are included in the branding document. Many thanks!

Industry/Entity Type

Environment

Font styles to use
Other font styles liked:
• As per our attached fonts

Requirements
Must have
• Our attached branding guidelines gives our look and feel - Innovative / Dynamic / Vibrant / Reliable / Accessible / Connected.

```html
<!DOCTYPE html>
<html lang="en">
<head>
<meta charset="utf-8">
<title>TEK ZUN – Exhibition Stand</title>
<link href="https://fonts.googleapis.com/css2?family=Montserrat:wght@600;700;800&display=swap" rel="stylesheet">
<style>
  :root {
    --page-bg: #e9ebea;
    --teal: #7ccab6;
    --green: #66bd48;
    --mint: #8fd0a0;
    --white: #ffffff;
    --ink: #0d0d0d;
  }
  html, body {
    margin: 0;
    padding: 0;
    width: 810px;
    height: 1200px;
    overflow: hidden;
    background: var(--page-bg);
  }
  .canvas {
    position: relative;
    width: 810px;
    height: 1200px;
    display: flex;
    align-items: center;
    justify-content: center;
  }
  .stand-panel {
    position: relative;
    width: 810px;
    height: 608px;
    overflow: hidden;
    font-family: "Montserrat", Arial, sans-serif;
  }
  .panel-art {
    position: absolute;
    inset: 0;
    width: 100%;
    height: 100%;
  }
  .brand-name {
    position: absolute;
    left: 70px;
    top: 58px;
    margin: 0;
    font-size: 72px;
    font-weight: 800;
    letter-spacing: 1px;
    line-height: 1;
    color: var(--ink);
  }
  .brand-url {
    position: absolute;
    left: 71px;
    top: 150px;
    margin: 0;
    font-size: 28px;
    font-weight: 700;
    letter-spacing: 0.5px;
    color: var(--white);
  }
  .values {
    position: absolute;
    left: 70px;
    top: 270px;
    margin: 0;
    padding: 0;
    list-style: none;
    font-size: 36px;
    font-weight: 600;
    line-height: 37px;
    letter-spacing: 0.2px;
  }
  .values .value-light { color: var(--white); }
  .values .value-dark { color: var(--ink); }
</style>
</head>
<body>
  <main class="canvas">
    <section class="stand-panel">
      <svg class="panel-art" viewBox="0 0 810 608" aria-hidden="true">
        <defs>
          <linearGradient id="panelGradient" x1="0" y1="0" x2="1" y2="0">
            <stop offset="0" stop-color="var(--teal)"/>
            <stop offset="0.45" stop-color="#73c380"/>
            <stop offset="1" stop-color="var(--green)"/>
          </linearGradient>
          <linearGradient id="bubbleGradient" x1="0" y1="0" x2="1" y2="0">
            <stop offset="0" stop-color="#ffffff"/>
            <stop offset="1" stop-color="#ffffff" stop-opacity="0.15"/>
          </linearGradient>
        </defs>
        <rect width="810" height="608" fill="url(#panelGradient)"/>
        <circle class="bubble-large" cx="680" cy="64" r="160" fill="url(#bubbleGradient)"/>
        <circle class="bubble-small" cx="604" cy="442" r="79" fill="url(#bubbleGradient)"/>
        <circle class="bubble-corner" cx="124" cy="548" r="160" fill="url(#bubbleGradient)"/>
      </svg>

      <h1 class="brand-name">TEK ZUN</h1>
      <p class="brand-url">www.tekzun.ch</p>

      <ul class="values">
        <li class="value-light">INNOVATIVE</li>
        <li class="value-light">DYNAMIC</li>
        <li class="value-light">VIBRANT</li>
        <li class="value-dark">RELIABLE</li>
        <li class="value-dark">ACCESSIBLE</li>
        <li class="value-dark">CONNECTED</li>
      </ul>
    </section>
  </main>
</body>
</html>
```